Business Card for a Wedding Films Business

We require a business card design for our business 'Lewis Marrow Wedding Films'. The logo needs to look classy and high end.

Target Market(s)

Wedding Couples

Contact Information for Business Card

Lewis Marrow Wedding Films
07312 605 227
films@lewismarrowreels.com
www.lewismarrowreels.com

Facebook: @lewismarrowweddingfilms
Instagram: @lewismarrowfilms

Font styles to use
Sans Serif

Requirements
Must have
• Social media icons - Facebook and Instagram

```html
<!DOCTYPE html>
<html lang="en">
<head>
<meta charset="utf-8">
<title>Lewis Marrow Wedding Films – Business Card</title>
<link href="https://fonts.googleapis.com/css2?family=Jost:wght@500&family=Arimo:wght@400&display=swap" rel="stylesheet">
<style>
  :root {
    --ink: #0a0a0a;
    --paper: #ffffff;
    --page: #ffffff;
    --frame: #1a1a1a;
  }
  html, body {
    margin: 0;
    padding: 0;
    width: 750px;
    height: 1200px;
    overflow: hidden;
    background: var(--page);
  }
  .canvas {
    position: relative;
    width: 750px;
    height: 1200px;
  }
  .card {
    position: absolute;
    left: 113px;
    width: 525px;
    height: 300px;
    background: var(--paper);
    border: 1px solid var(--frame);
    box-sizing: border-box;
    overflow: hidden;
  }
  .card--front { top: 41px; }
  .card--back  { top: 370px; }

  .band {
    position: absolute;
    top: 0;
    bottom: 0;
    background: var(--ink);
  }
  .card--front .band--left  { left: 0;  width: 18px; }
  .card--front .band--right { right: 0; width: 19px; }
  .card--back .band--left   { left: 0;  width: 37px; }
  .card--back .band--right  { right: 0; width: 37px; }

  .wordmark {
    position: absolute;
    left: 0;
    right: 0;
    text-align: center;
    font-family: "Jost", sans-serif;
    font-weight: 500;
    color: var(--ink);
    text-transform: uppercase;
    line-height: 1;
  }
  .wordmark__name { display: block; }
  .wordmark__tag  { display: block; }

  .card--front .wordmark { top: 100px; }
  .card--front .wordmark__name { font-size: 20px; letter-spacing: 4.6px; }
  .card--front .wordmark__tag  { font-size: 9.5px; letter-spacing: 4.4px; margin-top: 6px; }

  .card--back .wordmark { top: 132px; }
  .card--back .wordmark__name { font-size: 28px; letter-spacing: 5.6px; }
  .card--back .wordmark__tag  { font-size: 12px; letter-spacing: 5.6px; margin-top: 12px; }

  .rule {
    position: absolute;
    left: 93px;
    width: 339px;
    top: 150px;
    height: 1.5px;
    background: var(--ink);
  }

  .contact {
    position: absolute;
    font-family: "Arimo", sans-serif;
    font-size: 13px;
    color: var(--ink);
    line-height: 21px;
    margin: 0;
    padding: 0;
    list-style: none;
  }
  .contact--direct { left: 47px; top: 219px; }
  .contact--social { right: 28px; top: 240px; text-align: right; }
  .contact li {
    display: flex;
    align-items: center;
    gap: 8px;
    white-space: nowrap;
  }
  .contact--social li { justify-content: flex-end; }
  .contact svg { width: 11px; height: 11px; flex: none; }
  .social-mark {
    width: 9px;
    height: 9px;
    flex: none;
    background: var(--ink);
  }
  .social-mark--round {
    background: none;
    border: 1.3px solid var(--ink);
    border-radius: 50%;
    box-sizing: border-box;
  }
</style>
</head>
<body>
<main class="canvas">

  <section class="card card--front" aria-label="Business card front">
    <div class="band band--left"></div>
    <div class="band band--right"></div>

    <div class="wordmark">
      <span class="wordmark__name">Lewis Marrow</span>
      <span class="wordmark__tag">Wedding Films</span>
    </div>

    <div class="rule"></div>

    <ul class="contact contact--direct">
      <li>
        <svg viewBox="0 0 16 16" aria-hidden="true"><path fill="currentColor" d="M3.6 1.2 6 3.6c.4.4.4 1 0 1.4L4.8 6.2c.9 2 2.9 4 5 5l1.2-1.2c.4-.4 1-.4 1.4 0l2.4 2.4c.4.4.4 1 0 1.4l-1.4 1.4C11.7 16.9 0 6.4 1 2.6L2.2 1.2c.4-.4 1-.4 1.4 0z"/></svg>
        07312 605 227
      </li>
      <li>
        <svg viewBox="0 0 16 16" aria-hidden="true"><rect x="1" y="3" width="14" height="10" fill="none" stroke="currentColor" stroke-width="1.4"/><path d="M1 3.5 8 9l7-5.5" fill="none" stroke="currentColor" stroke-width="1.4"/></svg>
        films@lewismarrowreels.com
      </li>
      <li>
        <svg viewBox="0 0 16 16" aria-hidden="true"><circle cx="8" cy="8" r="7" fill="currentColor"/><path d="M4 5c2 0 2 2 3 2s1 2 0 3-1 2-2 2M10 3c0 2 2 2 3 3M10 11c1 0 2-1 3-1" stroke="#fff" stroke-width="1.2" fill="none"/></svg>
        www.lewismarrowreels.com
      </li>
    </ul>

    <ul class="contact contact--social">
      <li><span class="social-mark" aria-hidden="true"></span>lewismarrowweddingfilms</li>
      <li><span class="social-mark social-mark--round" aria-hidden="true"></span>lewismarrowfilms</li>
    </ul>
  </section>

  <section class="card card--back" aria-label="Business card back">
    <div class="band band--left"></div>
    <div class="band band--right"></div>

    <div class="wordmark">
      <span class="wordmark__name">Lewis Marrow</span>
      <span class="wordmark__tag">Wedding Films</span>
    </div>
  </section>

</main>
</body>
</html>
```